Norvale Rentals and Supply Flyer

A4 flyer to send electronic to potential customer via email to tell them about Norvale Rentals.
We are start up company looking at sending companies a flyer to introduce the business.

No Folds required - just a standard A4 design

Target Market(s)

Concrete and construction companies

Industry/Entity Type

Construction Company

Font styles to use
Sans Serif

Colors
fbee3e

Requirements
Must have
• Norvale Logo
• Images provided
Nice to have
• Black and Yellow colour scheme
Should not have
• n/a

```html
<!DOCTYPE html>
<html lang="en">
<head>
<meta charset="utf-8">
<title>Norvale Rentals and Supply Flyer</title>
<link href="https://fonts.googleapis.com/css2?family=Anton&family=Oswald:wght@400;500;700&display=swap" rel="stylesheet">
<style>
  :root {
    --yellow: #f7cb0f;
    --black: #0b0b0b;
    --red: #c8202a;
    --white: #ffffff;
    --page: #ffffff;
    --rule: #7a7a7a;
    --photo-light: #9c9893;
    --photo-mid: #6e6662;
    --photo-dark: #3d3533;
    --product-light: #c9c9c9;
    --product-dark: #7d7d7d;
  }
  html, body {
    margin: 0;
    padding: 0;
    width: 1200px;
    height: 1200px;
    overflow: hidden;
    background: var(--page);
  }
  .flyer {
    position: absolute;
    left: 195px;
    top: 26px;
    width: 811px;
    height: 1148px;
    display: block;
  }
  .headline { font-family: "Anton", "Oswald", sans-serif; fill: var(--black); }
  .condensed { font-family: "Oswald", sans-serif; }
  .brand-name { font-family: "Oswald", sans-serif; font-weight: 700; fill: var(--yellow); }
  .subtitle { fill: var(--black); font-weight: 500; }
  .services { fill: var(--yellow); font-weight: 700; }
  .fine-print { fill: var(--white); font-weight: 400; }
  .contact { fill: var(--white); font-weight: 400; }
  .accent { fill: var(--yellow); }
  .promise { fill: var(--black); font-weight: 700; }
  .promise-beat { font-family: "Anton", sans-serif; fill: var(--red); }
  .supplier-label { fill: var(--white); font-weight: 400; }
  .supplier { fill: var(--black); font-weight: 700; }
  .rule { stroke: var(--rule); stroke-width: 1; }
  .divider { stroke: var(--black); stroke-width: 2; }
</style>
</head>
<body>
<svg class="flyer" viewBox="0 0 1014 1435" xmlns="http://www.w3.org/2000/svg">
  <defs>
    <linearGradient id="showroomTone" x1="0" y1="0" x2="0.8" y2="1">
      <stop offset="0" stop-color="var(--photo-light)"/>
      <stop offset="0.55" stop-color="var(--photo-mid)"/>
      <stop offset="1" stop-color="var(--photo-dark)"/>
    </linearGradient>
    <linearGradient id="productTone" x1="0" y1="0" x2="1" y2="1">
      <stop offset="0" stop-color="var(--product-light)"/>
      <stop offset="1" stop-color="var(--product-dark)"/>
    </linearGradient>
  </defs>

  <rect class="base" width="1014" height="1435" fill="var(--black)"/>

  <polygon class="band-top" points="0,0 516,0 771,237 51,420 0,367" fill="var(--yellow)"/>

  <polygon class="showroom-photo" role="img" aria-label="Warehouse showroom with rows of concrete grinders, saws, vacuums and drills on shelving"
           points="51,420 1014,206 1014,1097 611,1047" fill="url(#showroomTone)"/>

  <polygon class="band-bottom" points="611,1047 1014,1097 1014,1435 424,1435" fill="var(--yellow)"/>

  <rect class="product-photo" role="img" aria-label="Floor grinder with dust extractor vacuum"
        x="46" y="654" width="350" height="278" rx="6" fill="url(#productTone)"/>

  <text class="brand-name" x="825" y="95" font-size="44" text-anchor="middle" textLength="320" lengthAdjust="spacingAndGlyphs">NORVALE RENTALS</text>

  <text class="headline" x="46" y="177" font-size="72" textLength="553" lengthAdjust="spacingAndGlyphs">NORVALE RENTALS AND SUPPLY</text>
  <text class="condensed subtitle" x="39" y="217" font-size="28" textLength="565" lengthAdjust="spacingAndGlyphs">Concrete, Construction and Communication Hire Equipment</text>

  <text class="condensed services" x="293" y="986" font-size="23" text-anchor="middle" textLength="376" lengthAdjust="spacingAndGlyphs">Honing, Polishing, Cutting, Drilling, Demolition</text>
  <text class="condensed services" x="293" y="1017" font-size="23" text-anchor="middle" textLength="308" lengthAdjust="spacingAndGlyphs">and General Hire Equipment Available.</text>
  <line class="rule" x1="62" y1="1028" x2="530" y2="1028"/>
  <text class="condensed fine-print" x="293" y="1049" font-size="13" text-anchor="middle" textLength="414" lengthAdjust="spacingAndGlyphs">Diamond Consumable for sale- core barrels, diamond segments and specialized tooling</text>
  <text class="condensed fine-print" x="293" y="1070" font-size="13" text-anchor="middle" textLength="510" lengthAdjust="spacingAndGlyphs">Good old fashion customer service with over 15 year's experience in the concrete and construction industry.</text>
  <line class="rule" x1="62" y1="1080" x2="530" y2="1080"/>

  <text class="condensed contact" x="79" y="1213" font-size="25">Find us on <tspan class="accent">Linkup</tspan> and <tspan class="accent">Snapfeed</tspan></text>
  <text class="condensed contact accent" x="79" y="1249" font-size="25">Contact us:</text>
  <text class="condensed contact" x="79" y="1285" font-size="25">E : info@norvalerentals.com.au</text>
  <text class="condensed contact" x="79" y="1321" font-size="25">W : www.norvalerentals.com.au</text>
  <text class="condensed contact" x="79" y="1357" font-size="25">A : unit 4, 12 Quarry Rd Belmore 6071</text>
  <text class="condensed contact" x="79" y="1392" font-size="25">P : 0400 118 245</text>

  <text class="condensed promise" x="676" y="1120" font-size="46" letter-spacing="-2">We</text>
  <text class="condensed promise" x="698" y="1158" font-size="46" letter-spacing="-2">will</text>
  <text class="promise-beat" x="676" y="1247" font-size="104" textLength="174" lengthAdjust="spacingAndGlyphs">BEAT</text>
  <text class="condensed promise" x="676" y="1279" font-size="30" textLength="186" lengthAdjust="spacingAndGlyphs">any written quote</text>
  <text class="condensed promise" x="676" y="1311" font-size="30" textLength="230" lengthAdjust="spacingAndGlyphs">from our competitors.</text>

  <polygon class="supplier-tag" points="476,1329 580,1329 596,1343 580,1357 476,1357" fill="var(--black)"/>
  <text class="condensed supplier-label" x="488" y="1350" font-size="17">Our suppliers :</text>

  <text class="condensed supplier" x="524" y="1399" font-size="24" text-anchor="middle">GRITLINE</text>
  <line class="divider" x1="592" y1="1374" x2="592" y2="1408"/>
  <text class="condensed supplier" x="660" y="1399" font-size="24" text-anchor="middle">TOOLMARK</text>
  <line class="divider" x1="728" y1="1374" x2="728" y2="1408"/>
  <text class="condensed supplier" x="796" y="1399" font-size="24" text-anchor="middle">KESTRA</text>
  <line class="divider" x1="864" y1="1374" x2="864" y2="1408"/>
  <text class="condensed supplier" x="932" y="1399" font-size="24" text-anchor="middle">VELDTON</text>
</svg>
</body>
</html>
```